Youth deer hunt give away flyer.

We need a flyer designed for a youth deer hunt giveaway that we are doing. We are an Illinois whitetail deer hunting outfitter. We house and feed our clients as well as providing them with a guided deer hunt. It needs to include images as well as details about the giveaway. Im looking for a proffesional, looking flyer

Target Market(s)

rednecks, hunters

Industry/Entity Type

Hunting

Font styles to use
Serif
Sans Serif

Colors
000000
dbdbdb
ffffff
474747

Requirements
Must have
• not sure
Nice to have
• not sure
Should not have
• not sure

```html
<!DOCTYPE html>
<html lang="en">
<head>
<meta charset="utf-8">
<title>2018 Youth Firearm Hunt – Harlan Ridge Outfitting</title>
<link rel="stylesheet" href="https://fonts.googleapis.com/css2?family=Cinzel:wght@400;600&family=Jost:wght@400;500&display=swap">
<style>
  :root {
    --black: #000000;
    --charcoal: #151515;
    --coal: #1f1f1f;
    --slate: #474747;
    --silver: #dbdbdb;
    --white: #ffffff;
  }
  * { box-sizing: border-box; margin: 0; padding: 0; }
  html, body { width: 1200px; height: 1200px; overflow: hidden; }
  body { background: #e6e6e4; font-family: "Jost", sans-serif; color: var(--white); }

  .flyer {
    position: absolute; left: 175px; top: 20px;
    width: 850px; height: 1160px; overflow: hidden;
    background: radial-gradient(ellipse at 60% 55%, var(--coal), var(--charcoal) 70%, var(--black));
  }
  .hero { position: absolute; left: 0; top: 0; width: 850px; height: 600px; }

  .brand {
    position: absolute; left: 540px; top: 470px; width: 300px; text-align: center;
    font-family: "Cinzel", serif; font-weight: 400; color: var(--silver);
  }
  .brand__mark { width: 18px; height: 18px; border: 2px solid var(--silver); border-radius: 50%; margin: 0 auto 14px; }
  .brand__name { font-size: 27px; letter-spacing: 1px; line-height: 1; }
  .brand__sub { font-size: 11px; letter-spacing: 4px; margin-top: 6px; }

  .title {
    position: absolute; left: 90px; top: 608px;
    font-family: "Cinzel", serif; font-weight: 600; font-size: 41px; letter-spacing: 1px;
  }
  .perks { position: absolute; left: 100px; top: 688px; width: 700px; list-style: none; }
  .perks li {
    position: relative; padding-left: 30px; margin-bottom: 11px;
    font-family: "Cinzel", serif; font-size: 18px; letter-spacing: 1px; line-height: 1.15;
  }
  .perks li::before {
    content: ""; position: absolute; left: 4px; top: 5px; width: 10px; height: 10px;
    border: 1.5px solid var(--silver); border-radius: 50%;
  }
  .perks li span { display: inline-block; border-bottom: 1px solid var(--silver); padding-bottom: 4px; white-space: nowrap; }

  .footer {
    position: absolute; left: 0; bottom: 0; width: 850px; height: 215px;
    background: linear-gradient(180deg, #3c3c3c, var(--slate) 40%, #3e3e3e);
    border-top: 6px solid var(--silver);
    display: flex; padding: 22px 30px 0 30px;
  }
  .about { width: 290px; padding-right: 14px; border-right: 1px solid var(--silver); height: 150px; }
  .about h2 { font-family: "Cinzel", serif; font-weight: 400; font-size: 12px; letter-spacing: 1px; margin-bottom: 4px; }
  .about p { font-size: 9.5px; line-height: 1.35; text-align: justify; color: var(--silver); }
  .contact { width: 210px; padding: 0 16px; border-right: 1px solid var(--silver); height: 150px; }
  .contact h2 {
    font-family: "Cinzel", serif; font-weight: 400; font-size: 16px; letter-spacing: 1px;
    border-bottom: 1px solid var(--silver); padding-bottom: 4px; margin-bottom: 18px; display: inline-block;
  }
  .line { display: flex; align-items: flex-start; gap: 10px; font-size: 12px; line-height: 1.3; margin-bottom: 14px; color: var(--white); }
  .line svg { flex: none; margin-top: 2px; }
  .online { padding-left: 18px; }
  .online .line { font-size: 11px; margin-bottom: 12px; }
  .follow { display: flex; align-items: center; gap: 8px; margin: 14px 0 0 40px; font-size: 12px; }
  .follow i { width: 14px; height: 14px; background: var(--silver); display: inline-block; }
</style>
</head>
<body>
<main class="flyer">
  <svg class="hero" viewBox="0 0 850 600">
    <defs>
      <linearGradient id="scene" x1="0" y1="0" x2="0" y2="1">
        <stop offset="0" stop-color="#eceae7"/>
        <stop offset="0.35" stop-color="#c9bfa8"/>
        <stop offset="0.6" stop-color="#8f7a4e"/>
        <stop offset="1" stop-color="#5e5a2e"/>
      </linearGradient>
      <radialGradient id="subject" cx="0.55" cy="0.6" r="0.45">
        <stop offset="0" stop-color="#a4804f" stop-opacity="0.9"/>
        <stop offset="1" stop-color="#a4804f" stop-opacity="0"/>
      </radialGradient>
      <radialGradient id="camo" cx="0.78" cy="0.45" r="0.3">
        <stop offset="0" stop-color="#5b5442" stop-opacity="0.85"/>
        <stop offset="1" stop-color="#5b5442" stop-opacity="0"/>
      </radialGradient>
      <linearGradient id="cabin" x1="0" y1="0" x2="0" y2="1">
        <stop offset="0" stop-color="#f1f1ef"/>
        <stop offset="0.55" stop-color="#b58a4c"/>
        <stop offset="1" stop-color="#6f9a45"/>
      </linearGradient>
      <clipPath id="photoClip"><path d="M0,0 H812 C786,255 630,405 255,545 L0,458 Z"/></clipPath>
    </defs>
    <path d="M0,0 H825 C800,260 640,420 260,560 L0,470 Z" fill="var(--silver)"/>
    <g role="img" aria-label="Photo of a smiling hunter in camouflage with his harvested whitetail buck in a grass field" clip-path="url(#photoClip)">
      <rect width="850" height="600" fill="url(#scene)"/>
      <rect width="850" height="600" fill="url(#subject)"/>
      <rect width="850" height="600" fill="url(#camo)"/>
    </g>
    <circle cx="160" cy="455" r="82" fill="var(--white)"/>
    <circle role="img" aria-label="Photo of the private log cabin lodging" cx="160" cy="455" r="74" fill="url(#cabin)"/>
  </svg>

  <div class="brand">
    <div class="brand__mark"></div>
    <div class="brand__name">HARLAN RIDGE</div>
    <div class="brand__sub">OUTFITTING</div>
  </div>

  <h1 class="title">2018 YOUTH FIREARM HUNT</h1>
  <ul class="perks">
    <li><span>OCTOBER 6-8, 2018</span></li>
    <li><span>4 NIGHT STAY IN OUR PRIVATE CABIN THAT INCLUDE<br>MEALS FOR 2 PARENTS AND THE CHILD.</span></li>
    <li><span>GUIDED SHOTGUN HUNT ON STRICTLY MANAGED PROPERTIES.</span></li>
    <li><span>GROUND BLINDS IN PLACE</span></li>
    <li><span>PERMIT &amp; LICENSE FEES ARE THE HUNTERS RESPONSIBILITY.</span></li>
  </ul>

  <footer class="footer">
    <section class="about">
      <h2>ABOUT US</h2>
      <p>Harlan Ridge Outfitting is a family owned and operated deer hunting outfitter in west central Illinois. We offer low pressure, trophy whitetail hunts on privately owned farms across the region. Our family has lived and hunted this land for generations. Along with guided deer and turkey hunts, we also provide whitetail land consulting, scouting services, food plot plantings and more.</p>
    </section>
    <section class="contact">
      <h2>DALE HARLAN</h2>
      <div class="line">
        <svg width="10" height="13" viewBox="0 0 10 13"><path d="M5 0a5 5 0 0 1 5 5c0 3.5-5 8-5 8S0 8.5 0 5a5 5 0 0 1 5-5z" fill="var(--silver)"/><circle cx="5" cy="5" r="1.8" fill="var(--slate)"/></svg>
        <span>1840 Ridge Road<br>Millbrook, Illinois 62000</span>
      </div>
      <div class="line">
        <svg width="11" height="11" viewBox="0 0 11 11"><path d="M2 0l2 3-1 1.5a7 7 0 0 0 3.5 3.5L8 7l3 2-1.5 2C5 11 0 6 0 1.5z" fill="var(--silver)"/></svg>
        <span>(555)014-2290</span>
      </div>
    </section>
    <section class="online">
      <div class="line">
        <svg width="10" height="10" viewBox="0 0 10 10"><circle cx="5" cy="5" r="4" fill="none" stroke="var(--silver)" stroke-width="1.5"/></svg>
        <span>harlanridgeoutfitting@example.com</span>
      </div>
      <div class="line">
        <svg width="10" height="10" viewBox="0 0 10 10"><circle cx="5" cy="5" r="4.5" fill="var(--silver)"/></svg>
        <span>www.harlanridgeoutfitting.example</span>
      </div>
      <div class="follow"><i></i><span>Follow our pages</span></div>
    </section>
  </footer>
</main>
</body>
</html>
```